Ferris Contracting LLC Business Card Design

I am looking for a creative and unique business card design. We are a commercial construction general contractor. With the name "FERRIS" Contracting, I am hoping to see some neat designs that correlate with the name.

```html
<!DOCTYPE html>
<html lang="en">
<head>
<meta charset="UTF-8">
<title>Ferris Contracting LLC – Business Card</title>
<link href="https://fonts.googleapis.com/css2?family=Poppins:wght@400;700&display=swap" rel="stylesheet">
<style>
  :root {
    --bg: #2a2a2b;
    --card: #1c1d1f;
    --card-back: #18191b;
    --blue: #1e8fd8;
    --text: #e4e4e4;
    --muted: #bdbdbd;
    --rule: #6b6b6b;
  }
  * { box-sizing: border-box; margin: 0; padding: 0; }
  html, body { width: 1200px; height: 1108px; overflow: hidden; }
  body {
    background: var(--bg);
    font-family: "Poppins", sans-serif;
    position: relative;
  }
  .card {
    position: absolute;
    top: 194px;
    width: 500px;
    height: 720px;
    border-radius: 28px;
    overflow: hidden;
  }
  .card-front { left: 70px; background: var(--card); text-align: center; }
  .card-back { left: 630px; background: var(--card-back); }

  .brand {
    position: absolute;
    left: 0; right: 0; top: 150px;
    font-weight: 700;
    font-size: 52px;
    letter-spacing: 2px;
    color: var(--blue);
    line-height: 1.1;
  }
  .brand-sub { display: block; font-size: 20px; letter-spacing: 9px; }

  .person { position: absolute; left: 0; right: 0; top: 420px; }
  .person-name {
    font-weight: 700; font-size: 28px; color: var(--blue); letter-spacing: 0.5px;
  }
  .person-role { font-weight: 400; font-size: 17px; color: var(--muted); letter-spacing: 1px; }

  .icon-row {
    position: absolute; left: 50px; right: 50px; top: 510px;
    display: flex; align-items: center; justify-content: center; gap: 10px;
  }
  .icon-row .rule { flex: 1; height: 1px; background: var(--rule); }
  .icon {
    width: 34px; height: 34px; border-radius: 5px; background: var(--blue);
    display: flex; align-items: center; justify-content: center;
  }
  .contact {
    position: absolute; left: 0; right: 0; top: 560px;
    font-size: 19px; line-height: 1.4; color: var(--text);
  }
  .contact .web { color: var(--blue); }
  .divider {
    position: absolute; left: 90px; right: 90px; top: 656px;
    height: 1px; background: var(--rule);
  }
  .address {
    position: absolute; left: 0; right: 0; top: 666px;
    font-size: 17px; line-height: 1.35; color: var(--text);
  }

  .back-pattern {
    position: absolute; inset: 0;
    background: linear-gradient(135deg, #2a2b2d 0%, #141516 50%, #232426 100%);
  }
  .back-brand {
    position: absolute; left: 0; right: 0; top: 330px;
    text-align: center;
    font-weight: 700; font-size: 36px; letter-spacing: 2px;
    color: var(--blue);
  }
</style>
</head>
<body>
  <section class="card card-front">
    <div class="brand">FERRIS<span class="brand-sub">CONTRACTING</span></div>

    <div class="person">
      <p class="person-name">MARCUS HALE</p>
      <p class="person-role">MANAGING DIRECTOR</p>
    </div>

    <div class="icon-row">
      <span class="rule"></span>
      <span class="icon" aria-label="Phone">
        <svg width="18" height="18" viewBox="0 0 24 24"><path fill="#fff" d="M6.6 10.8a15 15 0 0 0 6.6 6.6l2.2-2.2c.3-.3.7-.4 1-.2 1.1.4 2.3.6 3.6.6.6 0 1 .4 1 1V20c0 .6-.4 1-1 1A17 17 0 0 1 3 4c0-.6.4-1 1-1h3.5c.6 0 1 .4 1 1 0 1.3.2 2.5.6 3.6.1.3 0 .7-.2 1z"/></svg>
      </span>
      <span class="icon" aria-label="Email">
        <svg width="18" height="18" viewBox="0 0 24 24"><rect x="2" y="5" width="20" height="14" rx="1" fill="none" stroke="#fff" stroke-width="2"/><path d="M2 6l10 7 10-7" fill="none" stroke="#fff" stroke-width="2"/></svg>
      </span>
      <span class="icon" aria-label="Website">
        <svg width="18" height="18" viewBox="0 0 24 24"><circle cx="12" cy="12" r="9" fill="none" stroke="#fff" stroke-width="2"/><path d="M3 12h18M12 3c3 3 3 15 0 18M12 3c-3 3-3 15 0 18" fill="none" stroke="#fff" stroke-width="1.5"/></svg>
      </span>
      <span class="rule"></span>
    </div>

    <div class="contact">
      <p>044-555 210 347</p>
      <p>info@ferrisbuild.com</p>
      <p>www.<span class="web">ferrisbuild</span>.com</p>
    </div>
    <div class="divider"></div>
    <div class="address">
      <p>88, Harbor Road Suite 4</p>
      <p>45190, Westland</p>
    </div>
  </section>

  <section class="card card-back">
    <div class="back-pattern" role="img" aria-label="Repeated tone-on-tone company mark pattern in dark grey"></div>
    <div class="back-brand">FERRIS</div>
  </section>
</body>
</html>
```